I m Looking to Demonstrate My Product Features via Design & Elements

My Dear Freinds,

I am looking to demonstrate the following features of my product via design & elements (for my Orvelia listing)
https://www.orvelia-shop.example/dp/Q7XK2PLM4R/ref=tzu_c_3_k

1) Soft Touch - Skin Friendly Silky Soft Lining Inner Brushed Fleece

2) Stretchable - Four-way Stretch for Unrestricted Movement

3) Breathable - Moisture Control Odor Resistant

4) Quick-Drying - Sweat Wicking and Quick Dry Performance

5) Moisture-Wicking - Excellent Mobility and Moisture-Wicking

6) Heat Retention - Excellent Thermal Retention

7) Ultra-Light & Comfortable for Daily Warmth

8) Wonderfully Warm - Extra Layer of Warmth Under Your Clothes,

9) Elastic waistband - For the Pants for a Comfortable Snug Fit

10) Shrinkage Controlled - For lasting size and shape

see attached some examples & ideas

P.S. it shouldn't be exactly the same because these are from my competitors

Target Market(s)

People on Orvelia who are looking to buy Thermal Underwear

Industry/Entity Type

Womens Clothing

Font styles to use
Serif

Colors

Designer to choose colors to be used in the design.

Requirements
Must have
• Needs to be attractive
Nice to have
• Ok
Should not have
• Ok

```html
<!DOCTYPE html>
<html lang="en">
<head>
<meta charset="utf-8">
<title>Thermal Set Features</title>
<link href="https://fonts.googleapis.com/css2?family=Montserrat:wght@400;800&display=swap" rel="stylesheet">
<style>
:root{--ink:#111;--icon:#3d2a78;--bg:#fff;--teal:#1a93ad;--fleece:#e6e6e2;--cream:#efeadd}
*{margin:0;padding:0;box-sizing:border-box}
html,body{width:1200px;height:784px;overflow:hidden;background:var(--bg)}
.canvas{position:relative;width:1200px;height:784px;font-family:"Montserrat",sans-serif;color:var(--ink)}
.photo{position:absolute;left:90px;top:100px;width:1010px;height:510px;z-index:0;
  background:
    radial-gradient(ellipse 14% 30% at 74% 38%,rgba(239,234,221,.95) 0%,rgba(239,234,221,0) 100%),
    radial-gradient(ellipse 36% 22% at 52% 66%,rgba(26,147,173,.55) 0%,rgba(26,147,173,0) 100%),
    radial-gradient(ellipse 50% 18% at 50% 86%,var(--fleece) 0%,rgba(255,255,255,0) 100%)}
.feature{position:absolute;width:230px;text-align:center;transform:translateX(-50%);z-index:1}
.feature svg{display:block;margin:0 auto 14px;width:70px;height:70px;fill:none;stroke:var(--icon);stroke-width:3;stroke-linecap:round;stroke-linejoin:round}
.feature h3{font-weight:800;font-size:17px;line-height:20px}
.feature p{font-size:15px;line-height:19px;letter-spacing:.4px}
.row-top{top:35px}.row-mid{top:289px}.row-bot{top:598px}
</style>
</head>
<body>
<div class="canvas">
  <div class="photo" role="img" aria-label="Photo: woman reclining on a white fluffy rug in a teal thermal top and leggings, with a cream knit blanket and an open book"></div>

  <div class="feature row-top" style="left:141px">
    <svg viewBox="0 0 72 72"><path d="M36 4v6M6 30h6M66 30h-6M30 6l6 6 6-6"/><circle cx="36" cy="30" r="14"/><path d="M33 30v26h14v-13l-6-3h-5z" fill="var(--icon)"/></svg>
    <h3>Soft Touch</h3><p>Skin Friendly Silky<br>Soft Lining<br>Inner Brushed Fleece</p>
  </div>
  <div class="feature row-top" style="left:391px">
    <svg viewBox="0 0 72 72"><path d="M8 16h56M8 28h56M8 40h56M8 52h56M16 8v56M28 8v56M40 8v56M52 8v56"/></svg>
    <h3>Stretchable</h3><p>Four-way Stretch for<br>Unrestricted Movement</p>
  </div>
  <div class="feature row-top" style="left:660px">
    <svg viewBox="0 0 72 72"><path d="M36 6v34M36 30l-8 8M36 30l8 8M28 24c-10 0-20 14-20 34h18V32M44 24c10 0 20 14 20 34H46V32"/></svg>
    <h3>Breathable</h3><p>Moisture Control<br>Odor Resistant</p>
  </div>
  <div class="feature row-top" style="left:1032px">
    <svg viewBox="0 0 72 72"><path d="M16 20l8-4h12l8 4v22H16z" fill="var(--icon)"/><path d="M40 40h24M40 46h24M40 52h24M40 58h24M30 6v6"/></svg>
    <h3>Quick-Drying</h3><p>Sweat Wicking and<br>Quick Dry<br>Performance</p>
  </div>
  <div class="feature row-mid" style="left:141px">
    <svg viewBox="0 0 72 72"><path d="M24 8a6 6 0 0 1 12 0v38a11 11 0 1 1-12 0z"/><circle cx="30" cy="56" r="5"/><path d="M30 46V20"/><circle cx="54" cy="16" r="6"/></svg>
    <h3>Heat Retention</h3><p>Excellent Thermal<br>Retention</p>
  </div>
  <div class="feature row-mid" style="left:1032px">
    <svg viewBox="0 0 72 72"><circle cx="32" cy="30" r="20"/><path d="M20 28h36v20a4 4 0 0 1-4 4H24a4 4 0 0 1-4-4z"/><path d="M22 36h32"/></svg>
    <h3>Moisture-Wicking</h3><p>Excellent Mobility<br>and Moisture-Wicking</p>
  </div>
  <div class="feature row-bot" style="left:141px">
    <svg viewBox="0 0 72 72"><path d="M36 46l-10-10a6 6 0 0 1 10-6 6 6 0 0 1 10 6z"/><path d="M8 50h12l10 6h12M64 22H52L42 16H30"/><circle cx="36" cy="36" r="22" stroke-dasharray="3 5"/></svg>
    <h3>Ultra-Light</h3><p>Comfortable for<br>Daily Warmth</p>
  </div>
  <div class="feature row-bot" style="left:391px">
    <svg viewBox="0 0 72 72"><circle cx="36" cy="36" r="16"/><path d="M36 6v10M36 56v10M6 36h10M56 36h10M15 15l7 7M50 50l7 7M15 57l7-7M50 22l7-7"/></svg>
    <h3>Wonderfully Warm</h3><p>Extra Layer of Warmth<br>Under Your Clothes,</p>
  </div>
  <div class="feature row-bot" style="left:660px">
    <svg viewBox="0 0 72 72"><path d="M36 6v22M30 20l6 8 6-8M36 66V44M30 52l6-8 6 8M6 30q30 16 60 0M6 44q30-14 60 0"/></svg>
    <h3>Elastic waistband</h3><p>For the Pants for a<br>Comfortable Snug Fit</p>
  </div>
  <div class="feature row-bot" style="left:1032px">
    <svg viewBox="0 0 72 72"><path d="M36 6v20M28 18l8 8 8-8M36 66V46M28 54l8-8 8 8M6 32h60M6 40h60"/></svg>
    <h3>Shrinkage Controlled</h3><p>For lasting size<br>and shape</p>
  </div>
</div>
</body>
</html>
```